依頼詳細
お客様と話をする際、代理店や営業マンがお客様にお見せして、瞬時にポイントがわかり、詳細まで見たくなる仕上がりにしたいと考えています。
記載項目
文字、文言は添付ファイルにでています。
記載したい文字や協調したい文言は、文字の大きさで表現していますので、参考
にしてください。
表面
配置や色使いはお任せ致します。ポイントが目に飛び込んでくる様な仕上げに
してください。
裏面
事例が4例でてます。ポイントは赤字にしてありますが、元の配置や文字ポイン
ト・色は無視
して頂いて結構です。ポイントがわかりやすい仕上がりでお願い致します。
グラフについても同様で、意味が同じであればどんな色でもOKです。

サイズ
A4
ページ数
両面
希望イメージ
シンプル 複雑
単色 カラフル
暗い 明るい
日常 高級
遊び心 厳粛
未来的 伝統的
女性的 男性的
希望する色
水色系、グレー系
納品ファイル
• イラストレーター形式 (.ai)
補足説明
構成やデザインについての変更は、ありませんが文字(数値)などの変更をお願いする事がありますので、その節には対応の程お願い致します。
ロゴは、aiファイルに貼ってあります。
■ 選んだ理由

本当に悩みましたが
今回の利用目的を考慮した結果です。

■ 提案者全員のお礼・コメント

本当に、迷いました。
また機会がございましたら、是非ご応募いただきます様お願い致します。
皆さま方の今後の活躍を期待しております。

```html
<!DOCTYPE html>
<html lang="ja">
<head>
<meta charset="UTF-8">
<title>新電力＋LEDの導入で経費DOWN！売上UP！</title>
<link href="https://fonts.googleapis.com/css2?family=Noto+Sans+JP:wght@400;500;700;900&display=swap" rel="stylesheet">
<style>
  :root {
    --blue: #1f74c2;
    --blue-dark: #135a9e;
    --sky: #e3f0f9;
    --sky-deep: #c9e1f2;
    --red: #d9362c;
    --ink: #2b2b2b;
    --white: #ffffff;
  }
  * { margin: 0; padding: 0; box-sizing: border-box; }
  html, body { width: 848px; height: 1200px; overflow: hidden; }
  body { font-family: "Noto Sans JP", sans-serif; background: var(--white); }
  .flyer {
    position: relative; width: 848px; height: 1200px; overflow: hidden;
    background: linear-gradient(180deg, #ffffff 0%, var(--sky) 40%, #f3f8fc 72%);
  }
  .lead {
    position: absolute; top: 26px; left: 0; width: 100%; text-align: center;
    color: var(--blue); font-size: 22px; font-weight: 700; letter-spacing: 1px;
  }
  .lead-rule {
    position: absolute; top: 64px; left: 130px; width: 588px; height: 2px; background: var(--blue); opacity: .5;
  }
  .headline-row {
    position: absolute; top: 88px; left: 0; width: 100%;
    display: flex; justify-content: center; align-items: center; gap: 10px;
    color: var(--blue); font-weight: 900; font-size: 48px;
  }
  .tag-box {
    background: var(--white); border: 3px solid var(--blue); border-radius: 6px;
    padding: 0 16px; line-height: 62px;
  }
  .plus { font-size: 44px; padding: 0 4px; }
  .headline-down, .headline-up {
    position: absolute; color: var(--blue); font-weight: 900; letter-spacing: 2px; white-space: nowrap;
  }
  .headline-down { top: 168px; left: 100px; font-size: 76px; }
  .headline-up { top: 256px; left: 390px; font-size: 70px; }
  .arrows { position: absolute; top: 150px; left: 0; width: 848px; height: 220px; }
  .product-scene {
    position: absolute; top: 360px; left: 330px; width: 518px; height: 520px;
    background: radial-gradient(ellipse at 60% 45%, #ffffff 0%, #e8f2f9 45%, var(--sky-deep) 100%);
  }
  .benefit {
    position: absolute; left: 40px; width: 380px;
    background: var(--blue); color: var(--white); padding: 14px 20px;
  }
  .benefit-sub { font-size: 26px; font-weight: 700; line-height: 1.3; white-space: nowrap; }
  .benefit-main { font-size: 44px; font-weight: 900; line-height: 1.2; letter-spacing: 1px; white-space: nowrap; }
  .benefit--power { top: 370px; }
  .benefit--bill { top: 490px; }
  .benefit--lamp { top: 610px; width: 400px; padding: 14px 18px; }
  .benefit--lamp .benefit-main { font-size: 38px; letter-spacing: 0; }
  .benefit-note { font-size: 13.5px; line-height: 1.6; margin-top: 10px; font-weight: 400; }
  .extra-mark {
    display: inline-block; background: var(--white); color: var(--blue); border-radius: 50%;
    font-size: 14px; width: 30px; height: 30px; line-height: 30px; text-align: center; vertical-align: middle; margin-left: 6px;
  }
  .cost-badge {
    position: absolute; top: 384px; left: 440px; width: 96px; padding: 8px 6px;
    background: var(--white); border: 2px solid var(--blue); border-radius: 10px;
    color: var(--blue); font-size: 17px; font-weight: 700; text-align: center; line-height: 1.3;
  }
  .plug-icon { position: absolute; top: 512px; left: 345px; }
  .about {
    position: absolute; top: 880px; left: 0; width: 100%; height: 320px; background: var(--white);
    padding: 22px 40px 0;
  }
  .about-text { font-size: 19px; line-height: 1.65; color: var(--ink); font-weight: 500; text-align: justify; }
  .brand {
    position: absolute; top: 1010px; left: 470px; display: flex; align-items: center; gap: 14px;
  }
  .brand-dot { width: 58px; height: 58px; border-radius: 50%; background: var(--blue); }
  .brand-name { color: var(--blue); font-size: 54px; font-weight: 900; line-height: 1; }
  .brand-roman { position: absolute; top: 1078px; left: 542px; color: var(--blue); font-size: 15px; font-weight: 700; letter-spacing: 1px; }
  .company {
    position: absolute; top: 1138px; left: 0; width: 808px; text-align: right; color: var(--ink);
  }
  .company-name { font-size: 22px; font-weight: 900; margin-right: 12px; }
  .company-address { font-size: 15px; font-weight: 500; }
</style>
</head>
<body>
<main class="flyer">
  <p class="lead">省エネ診断ができる新電力会社からの電気代削減の提案</p>
  <div class="lead-rule"></div>

  <div class="headline-row">
    <span class="tag-box">新電力</span>
    <span class="plus">＋</span>
    <span class="tag-box">LED</span>
    <span>の導入で</span>
  </div>

  <svg class="arrows" viewBox="0 0 848 220" aria-hidden="true">
    <path d="M740 20 Q760 95 690 130" fill="none" stroke="var(--red)" stroke-width="16" stroke-linecap="round"/>
    <polygon points="660,108 708,150 650,158" fill="var(--red)"/>
    <path d="M340 210 Q320 150 370 118" fill="none" stroke="var(--red)" stroke-width="16" stroke-linecap="round"/>
    <polygon points="392,98 388,150 346,118" fill="var(--red)"/>
  </svg>

  <h1 class="headline-down">経費DOWN!</h1>
  <h1 class="headline-up">売上UP!</h1>

  <div class="product-scene" role="img" aria-label="電卓と電源プラグ、LED電球の写真"></div>

  <section class="benefit benefit--power">
    <p class="benefit-sub">LED交換で</p>
    <p class="benefit-main">消費電力削減</p>
  </section>
  <div class="cost-badge">工事費も<br>安い!</div>

  <section class="benefit benefit--bill">
    <p class="benefit-sub">新電力導入で</p>
    <p class="benefit-main">電気代削減</p>
  </section>
  <svg class="plug-icon" width="60" height="54" viewBox="0 0 60 54" aria-hidden="true">
    <rect x="18" y="10" width="26" height="26" rx="4" fill="var(--white)"/>
    <rect x="24" y="0" width="4" height="12" fill="var(--white)"/>
    <rect x="34" y="0" width="4" height="12" fill="var(--white)"/>
    <path d="M31 36 V46 Q31 52 24 52 H2" fill="none" stroke="var(--white)" stroke-width="4"/>
  </svg>

  <section class="benefit benefit--lamp">
    <p class="benefit-sub">LED導入による<span class="extra-mark">更に</span></p>
    <p class="benefit-main">管球交換コスト削減</p>
    <p class="benefit-note">蛍光灯の寿命が10,000時間、LEDの寿命が40,000時間とした場合、交換費用は約4分の1。白熱球の寿命は約6分の1と短く約2,000時間とした場合の交換費用は約20分の1。交換箇所が100箇所の場合の費用を計算すると大きな差がでます。</p>
  </section>

  <section class="about">
    <p class="about-text">ミナモ電力の関連団体は、経産省・環境省・グリーンネット都市・省エネセンター各機関の無料省エネ診断の診断事業者です。数多くの診断の実績がある新電力会社だからこそ、お客様の立場で考えお客様が喜ぶ提案をする事ができるのです。</p>
  </section>

  <div class="brand">
    <span class="brand-dot"></span>
    <span class="brand-name">ミナモ電力</span>
  </div>
  <p class="brand-roman">Minamo Lightworks</p>

  <p class="company">
    <span class="company-name">株式会社青葉ライトワークス</span>
    <span class="company-address">東京都千代田区架空町1-2-3</span>
  </p>
</main>
</body>
</html>
```